Upmarket Bathroom and Kitchen ware supplier needs a classy business card design

We are a company based in Fiji, we sell plumbing ware (Kitchen and bathroom taps, Basins,showers, toilets etc) through up market show rooms to individuals and directly through Architects and designers of resorts and holiday houses for new builds and renovations. we are wanting to upgrade our over all look and brand. we are starting with a new logo but will be rebranding the whole business. This project is for a business card design for my management and tales team I would like it to be dark, classy and interesting

Target Market(s)

Resort directors and Management, High end holiday home owners

Contact Information for Business Card

Neil Dawson
Director
+64219473815

Colors

Designer to choose colors to be used in the design.

Requirements
Must have
• Must have an upmarket appearance I like darker charcoal shades but will be guided by the designers
• Please any catch phrases like "Crafting remarkable living rooms" this belongs tpo one of our suppliers so can not be used.
Nice to have
• Double sided, so front dedicated to logo provided and back info about the business and the person.

```html
<!DOCTYPE html>
<html lang="en">
<head>
<meta charset="utf-8">
<title>Coralstone Interiors – Business Card</title>
<link rel="stylesheet" href="https://fonts.googleapis.com/css2?family=Arimo:wght@400;700&family=Open+Sans:wght@400&display=swap">
<style>
  :root {
    --page: #ffffff;
    --card-core: #262323;
    --ink-dark: #1a1a1a;
    --ink-light: #ffffff;
    --bleed-label: #5d4a3e;
    --icon-orange: #e8862a;
    --tan-bleed: #dcc796;
    --gold: #c6a43f;
    --yellow-bleed: #fed78f;
    --yellow: #fbb124;
    --orange-bleed: #f9ae84;
    --orange: #f26a24;
    --orange-deep: #f15a24;
    --orange-soft: #f57a3b;
    --salmon: #f9a982;
    --lemon-bleed: #fee39a;
    --lemon: #fdc72a;
    --lemon-mid: #fed24f;
  }
  html, body {
    margin: 0;
    padding: 0;
    width: 1200px;
    height: 1200px;
    overflow: hidden;
    background: var(--page);
  }
  .sheet { display: block; width: 1200px; height: 1200px; }
  .bleed-label { font-family: "Arimo", sans-serif; font-size: 31px; }
  .front .bleed-label { fill: var(--bleed-label); }
  .back .bleed-label { fill: #8b6f60; }
  .brand-name {
    font-family: "Open Sans", sans-serif;
    fill: var(--ink-light);
    font-weight: 400;
  }
  .brand-mark { fill: none; stroke: var(--ink-light); stroke-width: 4; }
  .front-url { font-family: "Open Sans", sans-serif; font-size: 34px; fill: var(--ink-dark); }
  .person-name { font-family: "Arimo", sans-serif; font-weight: 700; font-size: 40px; fill: var(--ink-light); }
  .person-role { font-family: "Arimo", sans-serif; font-size: 27px; fill: var(--ink-light); letter-spacing: 1px; }
  .contact-text { font-family: "Open Sans", sans-serif; fill: var(--ink-dark); }
  .contact-web { font-family: "Open Sans", sans-serif; fill: var(--ink-light); font-size: 30px; }
  .icon-dark { fill: none; stroke: var(--ink-dark); stroke-width: 3; stroke-linecap: round; stroke-linejoin: round; }
  .icon-dark-fill { fill: var(--ink-dark); }
  .icon-orange { fill: none; stroke: var(--icon-orange); stroke-width: 3; }
</style>
</head>
<body>
<svg class="sheet" viewBox="0 0 1500 1500" xmlns="http://www.w3.org/2000/svg">
  <defs>
    <linearGradient id="bleed-grey" x1="0" y1="0" x2="1" y2="0">
      <stop offset="0" stop-color="#6b6868"/>
      <stop offset="0.03" stop-color="#9a9a9a"/>
      <stop offset="0.1" stop-color="#6b6868"/>
      <stop offset="0.9" stop-color="#6b6868"/>
      <stop offset="1" stop-color="#979797"/>
    </linearGradient>
    <radialGradient id="card-glow" cx="0.5" cy="0.45" r="0.65">
      <stop offset="0" stop-color="#2a2727"/>
      <stop offset="0.6" stop-color="#1c1a1a"/>
      <stop offset="1" stop-color="#000000"/>
    </radialGradient>
    <linearGradient id="row-phone" x1="0" y1="0" x2="1" y2="0">
      <stop offset="0" stop-color="#7d6744"/>
      <stop offset="1" stop-color="#ad9a6f"/>
    </linearGradient>
    <linearGradient id="row-mail" x1="0" y1="0" x2="1" y2="0">
      <stop offset="0" stop-color="#c0813a"/>
      <stop offset="1" stop-color="#dc9e45"/>
    </linearGradient>
    <linearGradient id="row-address" x1="0" y1="0" x2="1" y2="0">
      <stop offset="0" stop-color="#dd6a26"/>
      <stop offset="1" stop-color="#ea8630"/>
    </linearGradient>
  </defs>

  <!-- Front side -->
  <g class="front">
    <rect class="card-bleed" x="163" y="42" width="1125" height="675" fill="url(#bleed-grey)"/>
    <rect class="card-trim" x="200" y="79" width="1050" height="600" fill="url(#card-glow)"/>

    <g class="top-bands">
      <polygon points="712,42 1288,42 1288,145 805,145" fill="var(--orange-bleed)"/>
      <polygon points="745,79 1250,79 1250,145 805,145" fill="var(--orange)"/>
      <polygon points="163,42 712,42 795,124 163,124" fill="var(--tan-bleed)"/>
      <polygon points="200,79 745,79 795,124 200,124" fill="var(--gold)"/>
      <polygon points="712,42 810,42 875,124 795,124" fill="var(--yellow-bleed)"/>
      <polygon points="745,79 840,79 875,124 795,124" fill="var(--yellow)"/>
    </g>

    <g class="bottom-bands">
      <polygon points="330,583 1065,583 1150,679 410,679" fill="var(--orange-deep)"/>
      <polygon points="330,583 510,583 605,679 410,679" fill="var(--orange-soft)"/>
      <polygon points="400,679 1150,679 1182,717 520,717" fill="var(--salmon)"/>
      <polygon points="163,625 440,625 525,717 163,717" fill="var(--lemon-bleed)"/>
      <polygon points="200,625 365,625 415,679 200,679" fill="var(--lemon)"/>
      <polygon points="365,625 440,625 490,679 415,679" fill="var(--lemon-mid)"/>
    </g>

    <text class="bleed-label" x="1030" y="71">Bleed Area</text>

    <g class="brand">
      <circle class="brand-mark" cx="440" cy="330" r="58"/>
      <text class="brand-name" x="530" y="343" font-size="30" letter-spacing="5">CORALSTONE INTERIORS</text>
    </g>

    <text class="front-url" x="820" y="632" text-anchor="middle">www.coralstonebath.com</text>
  </g>

  <!-- Back side -->
  <g class="back">
    <rect class="card-bleed" x="163" y="771" width="1125" height="675" fill="url(#bleed-grey)"/>
    <rect class="card-trim" x="200" y="808" width="1050" height="600" fill="url(#card-glow)"/>

    <g class="top-bands">
      <polygon points="640,771 1288,771 1288,920 760,920" fill="#dba07e"/>
      <polygon points="660,808 1250,808 1250,920 760,920" fill="#c05a2a"/>
      <polygon points="163,771 640,771 715,872 163,872" fill="#d9c490"/>
      <polygon points="200,808 660,808 715,872 200,872" fill="#ba973a"/>
      <polygon points="640,771 910,771 995,872 715,872" fill="#f5cf8c"/>
      <polygon points="660,808 945,808 995,872 715,872" fill="#eea733"/>
    </g>

    <text class="bleed-label" x="1030" y="800">Bleed Area</text>

    <g class="person">
      <text class="person-name" x="277" y="950">Neil Dawson</text>
      <text class="person-role" x="277" y="985">Director</text>
    </g>

    <g class="contact-rows">
      <polygon points="186,1070 597,1070 655,1138 186,1138" fill="url(#row-phone)"/>
      <polygon points="186,1138 655,1138 712,1204 186,1204" fill="url(#row-mail)"/>
      <polygon points="186,1204 712,1204 795,1304 186,1304" fill="url(#row-address)"/>
    </g>

    <g class="contact-phone">
      <path class="icon-dark" d="M282,1096 c-6,6 -4,18 6,28 c10,10 20,12 26,6 l-7,-8 l-6,3 c-4,-2 -10,-8 -12,-12 l3,-6 z"/>
      <path class="icon-dark" d="M296,1094 a12,12 0 0 1 12,12 M296,1087 a19,19 0 0 1 19,19"/>
      <text class="contact-text" x="352" y="1120" font-size="30">+64219473815</text>
    </g>

    <g class="contact-mail">
      <rect class="icon-dark" x="279" y="1165" width="30" height="22"/>
      <path class="icon-dark" d="M279,1165 l15,12 l15,-12 M279,1187 l12,-10 M309,1187 l-12,-10"/>
      <circle class="icon-dark" cx="294" cy="1160" r="6"/>
      <text class="contact-text" x="352" y="1183" font-size="30">mail@coralstone.fj</text>
    </g>

    <g class="contact-address">
      <path class="icon-dark-fill" d="M294,1264 l-13,-22 a15,15 0 1 1 26,0 z"/>
      <circle cx="294" cy="1241" r="6" fill="#e27628"/>
      <text class="contact-text" x="352" y="1242" font-size="27">48/B, Coral Bay Road,</text>
      <text class="contact-text" x="352" y="1277" font-size="27">Nadi Town, Fiji.</text>
    </g>

    <g class="contact-web-row">
      <circle class="icon-orange" cx="293" cy="1336" r="17"/>
      <ellipse class="icon-orange" cx="293" cy="1336" rx="7" ry="17"/>
      <path class="icon-orange" d="M276,1336 h34 M279,1326 h28 M279,1346 h28"/>
      <text class="contact-web" x="349" y="1346">www.coralstone.fj</text>
    </g>

    <g class="brand">
      <circle class="brand-mark" cx="818" cy="1112" r="44"/>
      <text class="brand-name" x="882" y="1122" font-size="21" letter-spacing="3">CORALSTONE INTERIORS</text>
    </g>
  </g>
</svg>
</body>
</html>
```